Carpet Cleaning Door Hanger Design Project

please design a door hanger for us. we do carpet cleaning. our company name is Velta Rug Works. our telephone number is 866-402-5719.

please make a special offer coupon.

please add bullets containing the following info-
Professional carpet, hardwood, tile & grout deep steam cleaning.
kid & pet safe.
fast drying.
100% eco friendly / toxin free products.
pet stain/s & odor control.
same day appointments.
clean uniformed employees.
and please put few other catchy lines.

please make a $20.00 of carpet cleaning coupon (restrictions apply).
please make a rooms starting at $59.99 (restrictions apply).

please also put- when you want the best for less call velta rug works.

Target Market(s)

home owners, home renters. new home buyers. new home sellers.

Industry/Entity Type

Home Improvement

Requirements
Must have
• special offer.
• double sided.
• must be a design for a door hanger.
Nice to have
• 100% satisfaction guaranteed bubble.
Should not have
• no website please

```html
<!DOCTYPE html>
<html lang="en">
<head>
<meta charset="utf-8">
<title>Velta Rug Works – Door Hanger</title>
<link href="https://fonts.googleapis.com/css2?family=Open+Sans:wght@600;700;800&family=Roboto+Condensed:wght@400;700&family=Oswald:wght@500;600&display=swap" rel="stylesheet">
<style>
  :root{
    --canvas:#e9e8e6;
    --white:#ffffff;
    --green:#3f9a36;
    --green-dark:#2a7a2a;
    --green-light:#8cc63f;
    --title-green:#3aa84a;
    --ink-green:#1f6b2a;
    --gold:#f0b323;
    --yellow:#f6e21a;
    --text-dark:#222;
  }
  *{box-sizing:border-box;margin:0;padding:0}
  html,body{width:1179px;height:1200px;overflow:hidden;background:var(--canvas)}
  .canvas{position:relative;width:1179px;height:1200px}
  .hanger{position:absolute;top:80px;width:419px;height:1020px;transform:scale(1.029);transform-origin:top left;background:var(--white);overflow:hidden;box-shadow:0 4px 12px rgba(0,0,0,.18)}
  .hanger--front{left:121px}
  .hanger--back{left:630px}
  .hanger svg.art{position:absolute;inset:0;width:419px;height:1020px}
  .t{position:absolute;white-space:nowrap}
  .brand-title{top:6px;left:0;width:100%;text-align:center;font:800 33px/1 "Open Sans",sans-serif;color:var(--title-green);letter-spacing:.3px}
  .service-pill{top:389px;left:15px;width:392px;height:42px;border-radius:21px;background:var(--gold);display:flex;align-items:center;justify-content:center;font:700 22px/1 "Roboto Condensed",sans-serif;color:var(--white);box-shadow:0 2px 3px rgba(0,0,0,.25)}
  .service-line{left:0;width:100%;text-align:center;font:700 17.5px/1.3 "Open Sans",sans-serif;color:var(--white)}
  .service-cta{left:0;width:100%;text-align:center;font:800 19px/1 "Open Sans",sans-serif;color:var(--yellow)}
  .offer-head{left:75px;font:800 23px/1 "Open Sans",sans-serif;color:var(--ink-green)}
  .offer-price{display:flex;align-items:baseline;gap:8px;font:600 54px/1 "Oswald",sans-serif;letter-spacing:-1px;color:var(--ink-green)}
  .offer-small{font:600 21px/1 "Oswald",sans-serif;letter-spacing:0;color:var(--ink-green)}
  .offer-note{left:70px;font:400 15px/1 "Roboto Condensed",sans-serif;color:var(--text-dark)}
  .footer-name{right:9px;font:600 20px/1 "Roboto Condensed",sans-serif;color:var(--gold);text-align:right}
  .footer-line{right:9px;font:400 13.5px/1.3 "Roboto Condensed",sans-serif;color:var(--white);text-align:right}
  .footer-phone{right:9px;top:980px;display:flex;align-items:center;gap:6px;font:700 29px/1 "Open Sans",sans-serif;color:var(--gold)}
  .benefit-intro{top:458px;left:0;width:100%;text-align:center;font:700 19px/1.35 "Roboto Condensed",sans-serif;color:var(--gold)}
  .benefit-list{position:absolute;top:528px;left:13px;list-style:none}
  .benefit-list li{display:flex;align-items:center;gap:13px;height:40px;font:700 19.5px/1 "Roboto Condensed",sans-serif;color:var(--white)}
</style>
</head>
<body>
<main class="canvas">

  <!-- FRONT SIDE -->
  <section class="hanger hanger--front">
    <svg class="art" viewBox="0 0 419 1020">
      <defs>
        <linearGradient id="f-photo" x1="0" y1="0" x2="0" y2="1"><stop offset="0" stop-color="#e9ecef"/><stop offset=".6" stop-color="#f3ede6"/><stop offset="1" stop-color="#f7f7f5"/></linearGradient>
        <linearGradient id="f-room" x1="0" y1="0" x2="1" y2="1"><stop offset="0" stop-color="#eef0f1"/><stop offset="1" stop-color="#fbfbfa"/></linearGradient>
        <linearGradient id="f-green" x1="0" y1="0" x2="0" y2="1"><stop offset="0" stop-color="#3d9a34"/><stop offset="1" stop-color="#2f8a2c"/></linearGradient>
        <radialGradient id="f-chip" cx=".4" cy=".4" r=".7"><stop offset="0" stop-color="#d9d6d0"/><stop offset="1" stop-color="#8c8a86"/></radialGradient>
        <radialGradient id="gold-seal" cx=".4" cy=".35" r=".7"><stop offset="0" stop-color="#ffe27a"/><stop offset="1" stop-color="#e09a12"/></radialGradient>
        <radialGradient id="eco" cx=".4" cy=".35" r=".7"><stop offset="0" stop-color="#8fd14f"/><stop offset="1" stop-color="#2f8a2c"/></radialGradient>
      </defs>
      <rect x="0" y="118" width="419" height="230" fill="url(#f-photo)" role="img" aria-label="Photo: smiling girl and small dog lying on a white shag carpet"/>
      <rect x="0" y="540" width="419" height="370" fill="url(#f-room)" role="img" aria-label="Photo: soft-focus carpet being vacuumed in a bright living room"/>
      <path d="M0,300 C120,355 270,290 419,300 V340 C280,320 120,370 0,330Z" fill="var(--gold)"/>
      <path d="M0,322 C120,375 280,312 419,330 V556 C300,520 140,560 0,520Z" fill="url(#f-green)"/>
      <path d="M0,520 C140,560 300,520 419,556 V590 C300,548 130,598 0,548Z" fill="var(--gold)"/>
      <line x1="0" y1="738" x2="419" y2="738" stroke="var(--green)" stroke-width="1.5" stroke-dasharray="3 3"/>
      <path d="M0,880 C140,900 300,860 419,870 V1020 H0Z" fill="var(--green-light)"/>
      <path d="M0,900 C140,920 300,878 419,890 V1020 H0Z" fill="url(#f-green)"/>
      <circle cx="207" cy="112" r="73" fill="var(--canvas)"/>
      <line x1="0" y1="121" x2="134" y2="121" stroke="#333" stroke-width="1.2"/>
      <circle cx="342" cy="97" r="34" fill="url(#eco)" role="img" aria-label="Eco-friendly seal"/>
      <circle cx="372" cy="617" r="42" fill="url(#f-chip)" stroke="var(--white)" stroke-width="3" role="img" aria-label="Photo: vacuum head on carpet"/>
      <circle cx="372" cy="775" r="42" fill="url(#f-chip)" stroke="var(--white)" stroke-width="3" role="img" aria-label="Photo: upholstery being cleaned"/>
      <g fill="none" stroke-width="3">
        <rect x="12" y="610" width="36" height="36" stroke="var(--green-light)"/>
        <path d="M18,626 L28,640 L56,602" stroke="var(--gold)" stroke-width="7" stroke-linecap="round"/>
        <rect x="12" y="762" width="36" height="36" stroke="var(--green-light)"/>
        <path d="M18,778 L28,792 L56,754" stroke="var(--gold)" stroke-width="7" stroke-linecap="round"/>
      </g>
      <circle cx="79" cy="942" r="60" fill="url(#gold-seal)" stroke="#f7d04a" stroke-width="4" role="img" aria-label="Satisfaction guarantee seal"/>
      <circle cx="79" cy="942" r="40" fill="none" stroke="#fff3c4" stroke-width="2"/>
    </svg>

    <h1 class="t brand-title">VELTA RUG WORKS</h1>
    <div class="t service-pill">CARPET &amp; UPHOLSTERY CLEANING</div>
    <p class="t service-line" style="top:442px">Professional carpet, hardwood, tile, stone &amp;</p>
    <p class="t service-line" style="top:465px">grout deep steam cleaning</p>
    <p class="t service-cta" style="top:491px">Call us for your FREE quote today!</p>

    <p class="t offer-head" style="top:616px">CARPET CLEANING</p>
    <p class="t offer-price" style="top:646px;left:70px">$20.00 <span class="offer-small">OFF</span></p>
    <p class="t offer-note" style="top:706px">(restrictions apply)</p>

    <p class="t offer-head" style="top:768px">CARPET CLEANING</p>
    <p class="t offer-price" style="top:798px;left:75px"><span class="offer-small">STARTING AT</span>$59.99</p>
    <p class="t offer-note" style="top:858px">(restrictions apply)</p>

    <p class="t footer-name" style="top:916px">VELTA RUG WORKS</p>
    <p class="t footer-line" style="top:940px">When you want the best for less,</p>
    <p class="t footer-line" style="top:958px">Call VELTA RUG WORKS, LLC.</p>
    <p class="t footer-phone">
      <svg width="26" height="26" viewBox="0 0 26 26"><circle cx="13" cy="13" r="11.5" fill="none" stroke="var(--gold)" stroke-width="2.5"/><path d="M9,7 L11,7 L12,10 L10.5,11.5 C11.5,13.5 12.5,14.5 14.5,15.5 L16,14 L19,15 L19,17 C19,18 18,19 17,19 C11,18.5 7.5,15 7,9 C7,8 8,7 9,7Z" fill="var(--gold)"/></svg>
      (866) 402-5719
    </p>
  </section>

  <!-- BACK SIDE -->
  <section class="hanger hanger--back">
    <svg class="art" viewBox="0 0 419 1020">
      <defs>
        <linearGradient id="b-photo" x1="0" y1="0" x2="0" y2="1"><stop offset="0" stop-color="#cfdbe6"/><stop offset=".55" stop-color="#eee6e0"/><stop offset="1" stop-color="#f4f2ee"/></linearGradient>
        <linearGradient id="b-green" x1="0" y1="0" x2="0" y2="1"><stop offset="0" stop-color="#46a33a"/><stop offset=".5" stop-color="#3a962f"/><stop offset="1" stop-color="#2f8a2c"/></linearGradient>
        <radialGradient id="b-chip" cx=".4" cy=".4" r=".7"><stop offset="0" stop-color="#e6e4e0"/><stop offset="1" stop-color="#9a9792"/></radialGradient>
        <radialGradient id="b-gold" cx=".4" cy=".35" r=".7"><stop offset="0" stop-color="#ffe27a"/><stop offset="1" stop-color="#e09a12"/></radialGradient>
        <radialGradient id="b-eco" cx=".4" cy=".35" r=".7"><stop offset="0" stop-color="#8fd14f"/><stop offset="1" stop-color="#2f8a2c"/></radialGradient>
      </defs>
      <rect x="0" y="60" width="419" height="360" fill="url(#b-photo)" role="img" aria-label="Photo: mother and daughter lying on a clean carpet in a living room"/>
      <path d="M0,385 C130,430 300,375 419,405 V440 C300,410 130,460 0,420Z" fill="var(--green-light)"/>
      <path d="M0,402 C130,450 300,392 419,420 V1020 H0Z" fill="url(#b-green)"/>
      <path d="M0,875 C150,920 300,860 419,880 V905 C300,885 150,945 0,900Z" fill="var(--gold)"/>
      <path d="M0,898 C150,943 300,882 419,902 V1020 H0Z" fill="var(--green)"/>
      <rect x="0" y="0" width="419" height="60" fill="var(--white)"/>
      <circle cx="207" cy="112" r="73" fill="var(--canvas)"/>
      <line x1="0" y1="121" x2="134" y2="121" stroke="#333" stroke-width="1.2"/>
      <circle cx="342" cy="97" r="34" fill="url(#b-eco)" role="img" aria-label="Eco-friendly seal"/>
      <circle cx="333" cy="377" r="63" fill="url(#b-chip)" stroke="var(--white)" stroke-width="4" role="img" aria-label="Photo: steam cleaning wand on carpet"/>
      <circle cx="128" cy="819" r="43" fill="url(#b-chip)" stroke="var(--white)" stroke-width="3" role="img" aria-label="Photo: red wine stain on carpet"/>
      <circle cx="214" cy="815" r="45" fill="url(#b-chip)" stroke="var(--white)" stroke-width="3" role="img" aria-label="Photo: tile floor being machine cleaned"/>
      <circle cx="306" cy="819" r="43" fill="url(#b-chip)" stroke="var(--white)" stroke-width="3" role="img" aria-label="Photo: spilled coffee cup on carpet"/>
      <circle cx="74" cy="942" r="60" fill="url(#b-gold)" stroke="#f7d04a" stroke-width="4" role="img" aria-label="Satisfaction guarantee seal"/>
      <circle cx="74" cy="942" r="40" fill="none" stroke="#fff3c4" stroke-width="2"/>
    </svg>

    <h1 class="t brand-title">VELTA RUG WORKS</h1>
    <p class="t benefit-intro">Professional carpet, hardwood, tile, stone &amp;<br>group steam cleaning</p>
    <ul class="benefit-list">
      <li><svg width="30" height="28" viewBox="0 0 30 28"><rect x="1.5" y="6" width="20" height="20" fill="none" stroke="var(--white)" stroke-width="2.5"/><path d="M5,15 L11,23 L27,3" fill="none" stroke="var(--gold)" stroke-width="5" stroke-linecap="round"/></svg>Kid &amp; pet safe</li>
      <li><svg width="30" height="28" viewBox="0 0 30 28"><rect x="1.5" y="6" width="20" height="20" fill="none" stroke="var(--white)" stroke-width="2.5"/><path d="M5,15 L11,23 L27,3" fill="none" stroke="var(--gold)" stroke-width="5" stroke-linecap="round"/></svg>Fast drying</li>
      <li><svg width="30" height="28" viewBox="0 0 30 28"><rect x="1.5" y="6" width="20" height="20" fill="none" stroke="var(--white)" stroke-width="2.5"/><path d="M5,15 L11,23 L27,3" fill="none" stroke="var(--gold)" stroke-width="5" stroke-linecap="round"/></svg>100% Eco-friendly &amp; toxic-free products</li>
      <li><svg width="30" height="28" viewBox="0 0 30 28"><rect x="1.5" y="6" width="20" height="20" fill="none" stroke="var(--white)" stroke-width="2.5"/><path d="M5,15 L11,23 L27,3" fill="none" stroke="var(--gold)" stroke-width="5" stroke-linecap="round"/></svg>Pet odor &amp; Pet urine removal treatment</li>
      <li><svg width="30" height="28" viewBox="0 0 30 28"><rect x="1.5" y="6" width="20" height="20" fill="none" stroke="var(--white)" stroke-width="2.5"/><path d="M5,15 L11,23 L27,3" fill="none" stroke="var(--gold)" stroke-width="5" stroke-linecap="round"/></svg>Same day appointments</li>
      <li><svg width="30" height="28" viewBox="0 0 30 28"><rect x="1.5" y="6" width="20" height="20" fill="none" stroke="var(--white)" stroke-width="2.5"/><path d="M5,15 L11,23 L27,3" fill="none" stroke="var(--gold)" stroke-width="5" stroke-linecap="round"/></svg>Clean uniformed employees</li>
    </ul>

    <p class="t footer-name" style="top:916px">VELTA RUG WORKS</p>
    <p class="t footer-line" style="top:940px">When you want the best for less,</p>
    <p class="t footer-line" style="top:958px">Call VELTA RUG WORKS, LLC.</p>
    <p class="t footer-phone">
      <svg width="26" height="26" viewBox="0 0 26 26"><circle cx="13" cy="13" r="11.5" fill="none" stroke="var(--gold)" stroke-width="2.5"/><path d="M9,7 L11,7 L12,10 L10.5,11.5 C11.5,13.5 12.5,14.5 14.5,15.5 L16,14 L19,15 L19,17 C19,18 18,19 17,19 C11,18.5 7.5,15 7,9 C7,8 8,7 9,7Z" fill="var(--gold)"/></svg>
      (866) 402-5719
    </p>
  </section>

</main>
</body>
</html>
```